mortgage company professional business card

We would like to revamp our business card. Logos and current card attached.

Target Market(s)

white collar professionals

Industry/Entity Type

Mortgage Lender

Contact Information for Business Card

Looking for a sharp professional feel with white background for business card. No gloss. Looking for emboss.

Requirements
Must have
• -Professional touch
• -Emboss and raised lettering
• -Social media icons
• name, title, Phone, email, NMLS and web
• Complement logo and web

```html
<!DOCTYPE html>
<html lang="en">
<head>
<meta charset="utf-8">
<title>Loanwise Business Card</title>
<link rel="stylesheet" href="https://fonts.googleapis.com/css2?family=Open+Sans:wght@400;600&display=swap">
<style>
  :root {
    --backdrop: #e9eaec;
    --card: #ffffff;
    --navy: #3f4f86;
    --navy-deep: #3a3f7e;
    --green: #3daa4e;
    --ink: #2a2a2a;
    --muted: #555a66;
  }
  * { box-sizing: border-box; margin: 0; padding: 0; }
  html, body {
    width: 1200px; height: 960px; overflow: hidden;
    background: var(--backdrop);
    font-family: "Open Sans", sans-serif;
  }
  .business-card {
    position: absolute; left: 75px; top: 180px;
    width: 1050px; height: 600px;
    background: var(--card);
    box-shadow: 0 18px 40px rgba(0,0,0,0.18);
    overflow: hidden;
  }
  .brand {
    position: absolute; left: 60px; top: 110px;
    display: flex; align-items: center; gap: 14px;
  }
  .brand-mark { width: 46px; height: 46px; background: var(--navy); }
  .brand-text { display: flex; flex-direction: column; }
  .brand-name {
    font-size: 50px; font-weight: 600; color: var(--navy); line-height: 1;
  }
  .brand-tagline {
    font-size: 16px; color: var(--muted); margin-top: 6px; padding-left: 4px;
  }
  .social-links {
    position: absolute; right: 60px; top: 50px;
    display: flex; gap: 18px;
  }
  .social-links span {
    width: 46px; height: 46px; border-radius: 10px; background: var(--navy);
  }
  .rule {
    position: absolute; left: 0; width: 100%; height: 6px; background: var(--green);
  }
  .rule-top { top: 228px; }
  .rule-bottom { top: 402px; }
  .name-band {
    position: absolute; left: 0; top: 250px; width: 100%; height: 132px;
    background: linear-gradient(90deg, var(--navy), var(--navy-deep));
    color: #ffffff; text-align: center;
    display: flex; flex-direction: column; justify-content: center;
    padding-left: 260px;
  }
  .person-name { font-size: 62px; font-weight: 400; line-height: 1.05; letter-spacing: 0.5px; }
  .person-title { font-size: 26px; margin-top: 4px; }
  .contact-list {
    position: absolute; left: 520px; top: 436px;
    list-style: none; color: var(--ink); font-size: 21px; line-height: 1.55;
  }
  .postal-address {
    position: absolute; left: 0; bottom: 22px; width: 100%;
    text-align: center; color: var(--ink); font-size: 22px; padding-left: 200px;
  }
</style>
</head>
<body>
  <div class="business-card">
    <div class="brand">
      <div class="brand-mark"></div>
      <div class="brand-text">
        <span class="brand-name">Loanwise</span>
        <span class="brand-tagline">Home loans made clear.</span>
      </div>
    </div>

    <div class="social-links" aria-label="Social media profiles">
      <span></span><span></span><span></span><span></span>
    </div>

    <div class="rule rule-top"></div>
    <div class="name-band">
      <div class="person-name">Jonah Ellery</div>
      <div class="person-title">Managing Director</div>
    </div>
    <div class="rule rule-bottom"></div>

    <ul class="contact-list">
      <li>T: 0800 (555) 0142</li>
      <li>E: info@example.com</li>
      <li>W: www.example.com</li>
    </ul>

    <p class="postal-address">12345 Address Street City State Postcode Country</p>
  </div>
</body>
</html>
```